KGDB Business Card

Looking for a business card design to incorporate our branding. We want to only use the colors listing in the Branding Package (attached).
Updates

Target Market(s)

People who need their phone or device fixed.

Industry/Entity Type

Electronics

Contact Information for Business Card

Please use:

Bright Circuit Mending Depot LLC
3478 S Ridge Trail 2210 E
Suite 417
San Antonio, TX 78341

Marcus Delwyn, Store Manager

(210) 555-0143

Requirements
Must have
• Must include the colors that are contained within the Branding Package PDF file.

```html
<!DOCTYPE html>
<html lang="en">
<head>
<meta charset="utf-8">
<title>KGDB Business Card</title>
<link rel="stylesheet" href="https://fonts.googleapis.com/css2?family=Questrial&display=swap">
<style>
  :root {
    --orange: #f0521f;
    --charcoal: #55575a;
    --charcoal-dark: #3d3f42;
    --white: #ffffff;
    --black: #161616;
    --stage: #e6e4e1;
    --text-light: #f2f2f2;
  }
  * { box-sizing: border-box; margin: 0; padding: 0; }
  html, body {
    width: 1200px;
    height: 764px;
    overflow: hidden;
    background: var(--stage);
    font-family: "Questrial", sans-serif;
  }
  .canvas {
    position: relative;
    width: 1200px;
    height: 764px;
  }
  .card {
    position: absolute;
    top: 227px;
    width: 540px;
    height: 309px;
    overflow: hidden;
    box-shadow: 0 6px 18px rgba(0, 0, 0, 0.18);
  }
  .card-front { left: 40px; background: var(--white); }
  .card-back { left: 620px; background: var(--black); }

  .card-wave {
    position: absolute;
    inset: 0;
    width: 540px;
    height: 309px;
  }

  .brand {
    position: absolute;
    display: flex;
    align-items: center;
    gap: 10px;
  }
  .brand-mark {
    width: 30px;
    height: 30px;
    border-radius: 6px;
    background: var(--orange);
    flex: none;
  }
  .brand-name {
    color: var(--orange);
    font-size: 21px;
    line-height: 1.1;
    max-width: 230px;
  }
  .card-front .brand { left: 32px; top: 44px; }
  .card-back .brand { left: 50%; top: 50%; transform: translate(-50%, -50%); }
  .card-back .brand-name { max-width: 280px; font-size: 24px; }

  .contact-line {
    display: flex;
    align-items: flex-start;
    gap: 10px;
    color: var(--text-light);
    font-size: 14px;
    line-height: 1.3;
  }
  .icon-box {
    width: 14px;
    height: 14px;
    background: var(--orange);
    flex: none;
    margin-top: 2px;
  }
  .icon-box svg { display: block; width: 14px; height: 14px; }

  .address { position: absolute; left: 40px; top: 218px; }

  .divider {
    position: absolute;
    left: 262px;
    top: 140px;
    width: 2px;
    height: 130px;
    background: var(--text-light);
  }

  .person { position: absolute; left: 290px; top: 140px; }
  .person-name { color: var(--text-light); font-size: 19px; }
  .person-role { color: var(--orange); font-size: 11px; margin-top: 2px; }

  .phone { position: absolute; left: 290px; top: 212px; }
</style>
</head>
<body>
<main class="canvas">

  <section class="card card-front" aria-label="Business card front">
    <svg class="card-wave" viewBox="0 0 540 309" aria-hidden="true">
      <path d="M0,206 C160,202 250,128 330,86 C400,50 470,40 540,44 L540,309 L0,309 Z" fill="var(--charcoal)"/>
      <path d="M0,196 C160,192 250,118 330,76 C400,40 470,30 540,34" fill="none" stroke="var(--charcoal-dark)" stroke-width="2"/>
      <path d="M0,201 C160,197 250,123 330,81 C400,45 470,35 540,39" fill="none" stroke="#b9babc" stroke-width="1.5"/>
    </svg>

    <div class="brand">
      <span class="brand-mark"></span>
      <span class="brand-name">Bright Circuit Mending Depot</span>
    </div>

    <div class="contact-line address">
      <span class="icon-box">
        <svg viewBox="0 0 14 14"><path d="M7 2.5a3 3 0 0 0-3 3c0 2.2 3 5.8 3 5.8s3-3.6 3-5.8a3 3 0 0 0-3-3z" fill="var(--white)"/><circle cx="7" cy="5.5" r="1.1" fill="var(--orange)"/></svg>
      </span>
      <span>3478 S Ridge Trail 2210 E<br>Suite 417<br>San Antonio, TX 78341</span>
    </div>

    <div class="divider"></div>

    <div class="person">
      <p class="person-name">Marcus Delwyn</p>
      <p class="person-role">Store Manager</p>
    </div>

    <div class="contact-line phone">
      <span class="icon-box">
        <svg viewBox="0 0 14 14"><path d="M4.3 2.8l1.5 2-0.9 1.1c0.6 1.3 1.6 2.3 2.9 2.9l1.1-0.9 2 1.5-0.8 1.8c-3.9-0.2-7-3.3-7.2-7.2z" fill="var(--white)"/></svg>
      </span>
      <span>(210) 555-0143</span>
    </div>
  </section>

  <section class="card card-back" aria-label="Business card back">
    <div class="brand">
      <span class="brand-mark"></span>
      <span class="brand-name">Bright Circuit Mending Depot</span>
    </div>
  </section>

</main>
</body>
</html>
```